Package design needed for magnetic lashes

I would like for the design to match my logo color scheme. The brand name is Bo Renna. It will be a paper box.

About the product: It is a 5-pair eyelashes package box with 1 tweezer and 2 magnetic eyeliners included in the package.
The product is reusable, easy to apply and cruelty free. It is suitable for every type of eye. And you can do different looks with it.

The packaging can be made in English but the end result should be in Dutch so I hope it can be translated after. I will translate it.

I will add some examples of product packaging designs that I like.
If there are any questions, please don't hesitate to ask me.

```html
<!DOCTYPE html>
<html lang="nl">
<head>
<meta charset="utf-8">
<title>Bo Renna – Magnetische wimpern verpakking</title>
<link href="https://fonts.googleapis.com/css2?family=Montserrat:wght@300;400;500;600;700&family=Sacramento&display=swap" rel="stylesheet">
<style>
  :root{
    --bg:#fcefee;
    --blush:#e9d5d5;
    --blush-deep:#dfc3c2;
    --rose:#a87467;
    --rose-light:#c9a097;
    --ink:#5a3d38;
    --white:#fff8f6;
    --line:#f6ebe9;
  }
  *{box-sizing:border-box;margin:0;padding:0}
  html,body{width:1200px;height:834px;overflow:hidden;background:var(--bg)}
  body{font-family:"Montserrat",sans-serif;color:var(--ink);position:relative}

  .panel{position:absolute;top:157px;width:520px;height:520px;background:var(--blush);overflow:hidden}
  .panel--front{left:50px}
  .panel--back{left:630px;padding:26px 30px}

  /* front */
  .wave-pattern{position:absolute;inset:0;background:
      radial-gradient(ellipse at 55% 45%, var(--blush) 0%, var(--blush) 35%, var(--blush-deep) 100%)}
  .front-content{position:relative;height:100%;text-align:center}
  .claims{position:absolute;top:30px;left:0;right:0;font-size:9.5px;letter-spacing:.12em;color:var(--rose-light);text-transform:uppercase}
  .brand{position:absolute;top:86px;left:0;right:0;display:flex;justify-content:center;align-items:center;gap:12px}
  .brand__dot{width:44px;height:44px;border-radius:50%;background:var(--rose)}
  .brand__name{font-size:30px;font-weight:500;color:var(--rose);letter-spacing:.02em}
  .title{position:absolute;top:180px;left:0;right:0}
  .title__main{font-size:46px;font-weight:400;letter-spacing:.14em;color:var(--rose);line-height:1}
  .title__script{font-family:"Sacramento",cursive;font-size:78px;color:var(--white);line-height:1;margin-top:-18px}
  .contents{position:absolute;top:340px;left:40px;right:40px;display:flex;justify-content:space-between}
  .item{width:140px;display:flex;flex-direction:column;align-items:center;gap:14px}
  .item__art{width:78px;height:78px;border-radius:50%;border:1.5px solid var(--white);background:var(--blush-deep)}
  .item__label{font-size:12px;color:var(--rose);letter-spacing:.03em}

  /* back */
  .section-title{font-size:12px;font-weight:700;letter-spacing:.06em;text-align:center;color:var(--ink);text-transform:uppercase}
  .apply{border:1px solid var(--white);margin-top:10px;padding:14px 12px;display:flex;justify-content:space-between}
  .step{width:140px;text-align:center;font-size:9px;line-height:1.3;color:var(--ink)}
  .step__art{width:66px;height:66px;border-radius:50%;border:1.5px solid var(--white);background:var(--blush-deep);margin:0 auto 8px}
  .step__label{display:block;font-weight:700;color:var(--rose-light);font-size:9.5px}
  .remove{margin-top:16px;text-align:center;font-size:9.5px;line-height:1.35}
  .remove .step__label{margin-top:6px}
  .ingredients{margin-top:16px;text-align:center}
  .ingredients p{font-size:8.5px;line-height:1.45;margin-top:5px}
  .back-footer{position:absolute;left:30px;right:30px;bottom:24px;display:flex;justify-content:space-between;align-items:center}
  .brand--small{position:static;gap:7px}
  .brand--small .brand__dot{width:24px;height:24px}
  .brand--small .brand__name{font-size:16px}
  .recycle{width:28px;height:28px}
</style>
</head>
<body>

<section class="panel panel--front">
  <div class="wave-pattern" role="img" aria-label="Decoratief patroon van fijne golvende lijnen in roségoud"></div>
  <div class="front-content">
    <p class="claims">Gemakkelijk aan te brengen • Geen lijm nodig • Herbruikbaar</p>
    <div class="brand">
      <span class="brand__dot"></span>
      <span class="brand__name">Bo Renna</span>
    </div>
    <h1 class="title">
      <span class="title__main">MAGNETISCHE</span>
      <span class="title__script" style="display:block">wimpern</span>
    </h1>
    <ul class="contents" style="list-style:none">
      <li class="item"><span class="item__art" role="img" aria-label="Illustratie van een wimperstrip"></span><span class="item__label">5 paar wimpers</span></li>
      <li class="item"><span class="item__art" role="img" aria-label="Illustratie van een pincet"></span><span class="item__label">1 pincet</span></li>
      <li class="item"><span class="item__art" role="img" aria-label="Illustratie van twee eyeliners"></span><span class="item__label">2 magnetische eyeliners</span></li>
    </ul>
  </div>
</section>

<section class="panel panel--back">
  <h2 class="section-title">Toepassen</h2>
  <div class="apply">
    <div class="step">
      <div class="step__art" role="img" aria-label="Illustratie van een eyeliner die geschud wordt"></div>
      <span class="step__label">STAP 1:</span>Schud de vloeibare eyeliner ruim voor gebruik
    </div>
    <div class="step">
      <div class="step__art" role="img" aria-label="Illustratie van een oog met eyeliner"></div>
      <span class="step__label">STAP 2:</span>Solliciteer tenminste 2 laagjes eyeliner. Het is belangrijk om laat het drogen.
    </div>
    <div class="step">
      <div class="step__art" role="img" aria-label="Illustratie van een oog met wimpers"></div>
      <span class="step__label">STAP 3:</span>Buig de wimpers lichtjes en leg op de eyeliner. Lijn de magneet uit om te bevestigen.
    </div>
  </div>

  <div class="remove">
    <h2 class="section-title">Verwijderen</h2>
    <span class="step__label">STAP 1:</span>
    <p>Verwijder de wimpers voorzichtig vanaf de oogrand i.d. richting het midden.</p>
    <span class="step__label">STAP 2:</span>
    <p>Om wimpers te behouden voor langer gebruik, verwijdert u alle overgebleven wimpers van de magneten en bewaar ze terug in de doos.</p>
    <span class="step__label">STAP 3:</span>
    <p>Gebruik oogmake-up remover of ander water om de liner voorzichtig schoon te maken met een wattenstaafje of Q-tip.</p>
  </div>

  <div class="ingredients">
    <h2 class="section-title">Ingrediënten</h2>
    <p>Aqua · Acrylaten/Octylacrylamide Copolymeer · Propyleenglycol · Ethylhexyl Glycerin · Butyleenglycol · PEG-3 Sorbitaan Oleaat · Steareth-21 · Dimethicon · Geur · Caprylic/Capric Triglyceride · PVP · Sorbitansesquioleaat · BHT · Methylparabeen · Propylparabeen · Fenoxyethanol · CI 77266 D&amp;C zwart nr. 2 · CI 77499 zwart ijzeroxide</p>
  </div>

  <div class="back-footer">
    <div class="brand brand--small">
      <span class="brand__dot"></span>
      <span class="brand__name">Bo Renna</span>
    </div>
    <svg class="recycle" viewBox="0 0 28 28" aria-label="Recyclebaar">
      <g fill="none" stroke="var(--ink)" stroke-width="2.4" stroke-linecap="round">
        <path d="M9 8 L14 3 L19 8"/>
        <path d="M22 14 L25 21 L18 23"/>
        <path d="M9 24 L3 21 L6 14"/>
      </g>
      <circle cx="14" cy="15" r="4" fill="none" stroke="var(--ink)" stroke-width="2"/>
    </svg>
  </div>
</section>

</body>
</html>
```